Velmar Ops Business Cards

We need to design some upbeat business cards. We are an Industrial Rope Access Company/Height Safety Company that specialize in Rope Access, Confined Space, Anchor Points, Safety Systems, PPE Inspecions and Rigging.
Company name is Velmar Ops Ltd
Card is for Gareth Lomas the Company Director
His mobile number is 027 418 9072 and email is gareth@velmarops.co.nz. Website address is www.velmarops.co.nz.
We will post some pictures below to ensure you get a good idea of what we do.

```html
<!DOCTYPE html>
<html lang="en">
<head>
<meta charset="utf-8">
<title>Velmar Ops Business Cards</title>
<link rel="stylesheet" href="https://fonts.googleapis.com/css2?family=Saira:wght@300;700&family=Michroma&family=Exo+2:ital,wght@1,500;1,600;1,800&display=swap">
<style>
  :root {
    --navy: #1b1650;
    --navy-deep: #0f0b33;
    --navy-soft: #2c2766;
    --white: #ffffff;
    --mist: #d9d8e6;
    --edge: #5b5b66;
  }
  * { margin: 0; padding: 0; box-sizing: border-box; }
  html, body { width: 1200px; height: 1200px; overflow: hidden; background: var(--white); }
  .canvas { position: relative; width: 1200px; height: 1200px; }

  .card { position: absolute; width: 840px; height: 480px; border-radius: 32px; overflow: hidden; }

  /* Front */
  .card--front { left: 72px; top: 82px; background: var(--navy); color: var(--white); text-align: center; }
  .brand-name {
    position: absolute; left: 0; right: 0; top: 58px;
    font-family: "Saira", sans-serif; font-weight: 700; font-size: 76px; line-height: 1;
    letter-spacing: 1px;
  }
  .brand-tagline {
    position: absolute; left: 0; right: 0; top: 146px;
    font-family: "Saira", sans-serif; font-weight: 300; font-size: 19px; line-height: 24px;
    letter-spacing: 2.4px; color: var(--mist);
  }
  .person-name {
    position: absolute; left: 0; right: 0; top: 330px;
    font-family: "Michroma", sans-serif; font-size: 30px; font-variant: small-caps;
    letter-spacing: 3px;
  }
  .person-role {
    position: absolute; left: 0; right: 0; top: 378px;
    font-family: "Michroma", sans-serif; font-size: 20px; font-variant: small-caps;
    letter-spacing: 3px;
  }

  /* Back */
  .card--back { left: 294px; top: 623px; height: 481px; background: var(--white); border: 1px solid var(--edge); }
  .back-shape { position: absolute; left: -1px; top: -1px; }
  .contact-list { position: absolute; left: 28px; top: 128px; list-style: none; color: var(--white); }
  .contact-item { display: flex; align-items: center; height: 44px; font-family: "Exo 2", sans-serif; font-style: italic; font-weight: 600; white-space: nowrap; }
  .contact-item svg { width: 26px; height: 26px; margin-right: 14px; flex: none; }
  .contact-item--phone { font-size: 33px; }
  .contact-item--email { font-size: 26px; }
  .contact-item--web { font-size: 25px; font-weight: 800; letter-spacing: 5px; }
  .rope-placeholder {
    position: absolute; left: 0; top: 266px; width: 502px; height: 60px;
    background: linear-gradient(90deg, var(--navy-soft), var(--navy));
  }

  .services { position: absolute; left: 0; top: 0; color: var(--navy); font-family: "Exo 2", sans-serif; font-style: italic; }
  .services-title { position: absolute; left: 476px; top: 26px; font-size: 34px; font-weight: 500; white-space: nowrap; }
  .service { position: absolute; font-size: 24px; font-weight: 800; letter-spacing: 0.4px; white-space: nowrap; }
  .service::before { content: "·"; font-weight: 800; margin-right: 6px; }
</style>
</head>
<body>
<div class="canvas">

  <section class="card card--front">
    <div class="brand-name">Velmar Ops</div>
    <div class="brand-tagline">Safety &nbsp;|&nbsp; Integrity &nbsp;|&nbsp; Quality &nbsp;|&nbsp; Assurance</div>
    <div class="person-name">Gareth Lomas</div>
    <div class="person-role">Director</div>
  </section>

  <section class="card card--back">
    <svg class="back-shape" width="560" height="483" viewBox="0 0 560 483" aria-hidden="true">
      <path d="M0 0 H406 C590 110 590 372 406 483 H0 Z" fill="var(--navy)"/>
      <path d="M406 0 C530 110 530 372 406 483 C545 372 545 110 406 0 Z" fill="var(--navy-deep)" opacity="0.7"/>
    </svg>

    <ul class="contact-list">
      <li class="contact-item contact-item--phone">
        <svg viewBox="0 0 24 24"><path fill="#fff" d="M6.6 10.8a15.1 15.1 0 0 0 6.6 6.6l2.2-2.2c.3-.3.7-.4 1-.2 1.1.4 2.3.6 3.6.6.6 0 1 .4 1 1V20c0 .6-.4 1-1 1A17 17 0 0 1 3 4c0-.6.4-1 1-1h3.5c.6 0 1 .4 1 1 0 1.3.2 2.5.6 3.6.1.3 0 .7-.2 1z"/></svg>
        027 418 9072
      </li>
      <li class="contact-item contact-item--email">
        <svg viewBox="0 0 24 24"><path fill="#fff" d="M22 2 2 10.5l7 2.5 2.5 7L22 2zM9.6 12.4 18 6l-6.4 8.4z"/></svg>
        gareth@velmarops.co.nz
      </li>
      <li class="contact-item contact-item--web">
        <svg viewBox="0 0 24 24" fill="none" stroke="#fff" stroke-width="1.6"><circle cx="12" cy="12" r="10"/><ellipse cx="12" cy="12" rx="4.5" ry="10"/><path d="M2 12h20M4 7h16M4 17h16M12 2v20"/></svg>
        www.velmarops.co.nz
      </li>
    </ul>

    <div class="rope-placeholder" role="img" aria-label="Decorative rope with a tied loop running across the card"></div>

    <div class="services">
      <div class="services-title">We Specialize in :</div>
      <span class="service" style="left:530px;top:94px;">Rope Access</span>
      <span class="service" style="left:554px;top:146px;">Confined Space</span>
      <span class="service" style="left:566px;top:197px;">Safety Systems</span>
      <span class="service" style="left:564px;top:250px;">PPE Certification</span>
      <span class="service" style="left:552px;top:301px;">Anchor Points</span>
      <span class="service" style="left:536px;top:350px;">Rigging</span>
    </div>
  </section>

</div>
</body>
</html>
```